Energy trading company (Voltrisa) needs a business card

We need a business card for a company based in Central America. Our main purpose is trading energy . We already have the logo but we need some good creativity to design a high impact business card. Colors blue, orange, green can be used or we would like to see good combinatios with our logo

Target Market(s)

Energy

Industry/Entity Type

Power Generation

Contact Information for Business Card

Logo , headquarters , name, background

Font styles to use
Serif
Sans Serif

Colors

Designer to choose colors to be used in the design.

Requirements
Must have
• it must have a fresh and clean view
Nice to have
• good backgrounds that combine with the logo
Should not have
• too much words

```html
<!DOCTYPE html>
<html lang="en">
<head>
<meta charset="utf-8">
<title>Voltrisa Business Card</title>
<link rel="stylesheet" href="https://fonts.googleapis.com/css2?family=Open+Sans:wght@400;600;700&display=swap">
<style>
  :root {
    --backdrop: #4a4a4c;
    --card: #0d0d0f;
    --orange: #f5821f;
    --white: #ffffff;
  }
  * { margin: 0; padding: 0; box-sizing: border-box; }
  html, body {
    width: 1200px; height: 900px; overflow: hidden;
    background: var(--backdrop);
    font-family: "Open Sans", Arial, sans-serif;
  }
  .canvas {
    position: relative; width: 1200px; height: 900px;
    display: flex; flex-direction: column; align-items: center; justify-content: center;
    gap: 24px;
  }
  .card {
    position: relative; width: 700px; height: 400px;
    background: var(--card); border-radius: 26px;
  }
  .card-front { display: flex; align-items: center; justify-content: center; }
  .brand-name {
    color: var(--orange); font-weight: 600; letter-spacing: 2px;
    text-transform: uppercase; line-height: 1;
  }
  .card-front .brand-name { font-size: 84px; }
  .card-back .brand-name {
    position: absolute; right: 48px; top: 122px; font-size: 52px;
  }
  .holder { position: absolute; left: 44px; top: 168px; }
  .holder-name {
    color: var(--orange); font-weight: 700; font-size: 27px; letter-spacing: 1.5px;
    text-transform: uppercase;
  }
  .holder-role { color: var(--white); font-weight: 600; font-size: 20px; margin-top: 2px; }
  .divider {
    position: absolute; left: 140px; right: 48px; top: 228px;
    height: 1.5px; background: var(--orange);
  }
  .contact-list {
    position: absolute; left: 44px; top: 252px; list-style: none;
    color: var(--white); font-size: 19px;
  }
  .contact-list li { display: flex; align-items: center; gap: 12px; height: 34px; }
  .contact-list svg { width: 16px; height: 16px; flex: none; }
</style>
</head>
<body>
<main class="canvas">
  <section class="card card-front">
    <p class="brand-name">Voltrisa</p>
  </section>

  <section class="card card-back">
    <p class="brand-name">Voltrisa</p>
    <div class="holder">
      <h1 class="holder-name">Mateo Lind</h1>
      <p class="holder-role">Owner</p>
    </div>
    <div class="divider"></div>
    <ul class="contact-list">
      <li>
        <svg viewBox="0 0 16 16" aria-hidden="true"><path d="M3 1.5l2.5 0 1.2 3.2-1.6 1.2c.8 1.8 2.2 3.2 4 4l1.2-1.6 3.2 1.2v2.5c0 .8-.7 1.5-1.5 1.5C6.6 13.5 2.5 9.4 1.5 3 1.5 2.2 2.2 1.5 3 1.5z" fill="none" stroke="#f5821f" stroke-width="1.5"/></svg>
        (505) 218-4430
      </li>
      <li>
        <svg viewBox="0 0 16 16" aria-hidden="true"><rect x="1" y="3" width="14" height="10" rx="1" fill="none" stroke="#f5821f" stroke-width="1.6"/><path d="M1.5 3.5L8 9l6.5-5.5" fill="none" stroke="#f5821f" stroke-width="1.6"/></svg>
        info@voltrisa.com
      </li>
      <li>
        <svg viewBox="0 0 16 16" aria-hidden="true"><circle cx="8" cy="8" r="7" fill="#f5821f"/><path d="M1 8h14M8 1c-3 3.5-3 10.5 0 14M8 1c3 3.5 3 10.5 0 14" fill="none" stroke="#0d0d0f" stroke-width="1.2"/></svg>
        www.voltrisa.com
      </li>
    </ul>
  </section>
</main>
</body>
</html>
```